Law Firm Stationery Design - Traditional Meets Intuitive

Looking for a modern, yet classic, law firm stationery design. Simplicity is desired, but great ideas are encouraged. See attachment for company information. We utilize a variety of non-traditional legal tools to bring a different perspective to each of our client's particular situation. Final design should communicate classic values with intuitive, unique solutions.

Industry/Entity Type

Law Firm

Requirements
Should not have
• - No typical legal icons
• - No Tag Line!
• - DO NOT WANT WHAT WE ALREADY HAVE

```html
<!DOCTYPE html>
<html lang="en">
<head>
<meta charset="utf-8">
<title>Veritane Law — Business Card</title>
<link href="https://fonts.googleapis.com/css2?family=Libre+Caslon+Text&family=Source+Sans+3:wght@400;600;700&display=swap" rel="stylesheet">
<style>
  :root {
    --backdrop: #d7b48e;
    --paper: #ffffff;
    --brand-blue: #0768a8;
    --ink: #111111;
    --text-grey: #4a4a4a;
    --rule-grey: #8a8a8a;
    --serif: "Libre Caslon Text", Georgia, serif;
    --sans: "Source Sans 3", Arial, sans-serif;
  }
  * { margin: 0; padding: 0; box-sizing: border-box; }
  html, body { width: 1200px; height: 987px; overflow: hidden; }
  body { background: var(--backdrop); position: relative; font-family: var(--sans); }

  .card { position: absolute; width: 615px; height: 351px; }
  .card-front { left: 293px; top: 130px; background: var(--paper); }
  .card-back { left: 292px; top: 505px; height: 352px; background: var(--brand-blue); }

  .wordmark { position: absolute; text-align: right; }
  .wordmark-name { font-family: var(--serif); font-weight: 400; line-height: 1; white-space: nowrap; }

  .card-front .wordmark { right: 35px; top: 56px; }
  .card-front .wordmark-name { font-size: 40px; color: var(--ink); }

  .card-back .wordmark { right: 25px; top: 272px; }
  .card-back .wordmark-name { font-size: 36px; color: var(--paper); }

  .holder { position: absolute; left: 41px; top: 179px; }
  .holder-name { font-size: 22px; font-weight: 700; color: var(--ink); line-height: 1.1; }
  .holder-title { font-size: 17px; color: var(--brand-blue); line-height: 1.3; }

  .divider { position: absolute; left: 41px; right: 35px; top: 233px; height: 1px; background: var(--rule-grey); }

  .contact-list { position: absolute; left: 41px; top: 246px; list-style: none; }
  .contact-item { display: flex; align-items: center; height: 24px; font-size: 16px; color: var(--text-grey); }
  .contact-item svg { width: 14px; height: 14px; margin-right: 10px; flex: none; }

  .office { position: absolute; right: 35px; top: 248px; text-align: right; font-size: 16px; color: var(--text-grey); line-height: 24px; }
  .office-name { font-weight: 700; }

  .accent-bar { position: absolute; left: 0; bottom: 0; width: 615px; height: 12px; display: block; }
</style>
</head>
<body>

<section class="card card-front">
  <div class="wordmark">
    <div class="wordmark-name">Veritane Law</div>
  </div>

  <div class="holder">
    <div class="holder-name">DANIEL HART</div>
    <div class="holder-title">CEO/Founder</div>
  </div>

  <div class="divider"></div>

  <ul class="contact-list">
    <li class="contact-item">
      <svg viewBox="0 0 14 14" aria-hidden="true"><rect x="3" y="0.5" width="8" height="13" rx="1.2" fill="none" stroke="#222" stroke-width="1.6"/><rect x="5.5" y="10.5" width="3" height="1.2" fill="#222"/></svg>
      617-555-0148
    </li>
    <li class="contact-item">
      <svg viewBox="0 0 14 14" aria-hidden="true"><rect x="1" y="3" width="12" height="8" fill="#222"/><path d="M1 3 L7 8 L13 3" fill="none" stroke="#fff" stroke-width="1"/></svg>
      info@veritane.com
    </li>
    <li class="contact-item">
      <svg viewBox="0 0 14 14" aria-hidden="true"><circle cx="7" cy="7" r="6.3" fill="#222"/><path d="M4 4 Q6 5 5 7 Q7 8 6 11 M9 3 Q8 6 11 7" fill="none" stroke="#fff" stroke-width="1"/></svg>
      www.veritane.com
    </li>
  </ul>

  <div class="office">
    <div class="office-name">VERITANE LAW LLC</div>
    <div>18 Harbor Lane, Suite 300</div>
    <div>Easton, MA 02375</div>
  </div>

  <svg class="accent-bar" viewBox="0 0 615 12" aria-hidden="true">
    <polygon points="0,0 401,0 397,12 0,12" fill="var(--ink)"/>
    <polygon points="405,0 615,0 615,12 401,12" fill="var(--brand-blue)"/>
  </svg>
</section>

<section class="card card-back">
  <div class="wordmark">
    <div class="wordmark-name">Veritane Law</div>
  </div>
</section>

</body>
</html>
```